Brantmoor Financial Coaching LLC - Needed clean black business card

Business card for personal financial coaching practice located on Las Vegas NV, new startup. Back of card needs to have "how it works" to match the website.

Font styles to use
Sans Serif

Colors

Designer to choose colors to be used in the design.

```html
<!DOCTYPE html>
<html lang="en">
<head>
<meta charset="UTF-8">
<title>Brantmoor Financial Coaching LLC – Business Card</title>
<link rel="stylesheet" href="https://fonts.googleapis.com/css2?family=Montserrat:wght@700&family=Questrial&display=swap">
<style>
  :root {
    --page-bg: #e6e6e4;
    --card-dark: #121212;
    --card-mid: #1d1d1d;
    --ink: #f2f2f2;
    --ink-soft: #d6d6d6;
    --rule: #cfcfcf;
  }
  * { margin: 0; padding: 0; box-sizing: border-box; }
  html, body {
    width: 1200px;
    height: 800px;
    overflow: hidden;
    background: var(--page-bg);
  }
  .canvas {
    width: 1200px;
    height: 800px;
    display: flex;
    align-items: center;
    justify-content: center;
    gap: 40px;
  }
  .card {
    position: relative;
    width: 540px;
    height: 310px;
    overflow: hidden;
    background: linear-gradient(135deg, var(--card-mid) 0%, var(--card-dark) 100%);
    color: var(--ink);
    font-family: "Questrial", "Century Gothic", sans-serif;
    box-shadow: 0 12px 30px rgba(0, 0, 0, 0.18);
  }

  /* Back: How It Works */
  .card-back { padding: 84px 24px 0 40px; }
  .how-title {
    font-family: "Montserrat", "Century Gothic", sans-serif;
    font-weight: 700;
    font-size: 21px;
    letter-spacing: 0.5px;
  }
  .how-rule {
    width: 125px;
    height: 1px;
    background: var(--rule);
    margin: 10px 0 14px;
  }
  .how-steps {
    list-style: none;
    font-size: 12.6px;
    line-height: 25px;
    color: var(--ink-soft);
    letter-spacing: 0.1px;
    white-space: nowrap;
  }

  /* Front: identity */
  .card-front { padding: 50px 36px 0 42px; }
  .company-name {
    font-size: 28px;
    font-weight: 400;
    letter-spacing: 0.2px;
    white-space: nowrap;
  }
  .contact {
    margin: 36px 0 0 78px;
    font-size: 13px;
    line-height: 18px;
    color: var(--ink-soft);
  }
  .contact-rule {
    width: 140px;
    height: 1px;
    background: var(--rule);
    margin: 10px 0 12px;
  }
</style>
</head>
<body>
  <main class="canvas">
    <section class="card card-back" aria-label="Card back">
      <h2 class="how-title">How It Works</h2>
      <div class="how-rule"></div>
      <ul class="how-steps">
        <li>All free one-time consultations are in-person meetings only.</li>
        <li>Paid appointments may be scheduled for in-person or virtual meetings.</li>
        <li>Select the session, date and time that works best for your schedule.</li>
        <li>Start your journey of financial freedom at brantmoorfinancialcoaching.com</li>
      </ul>
    </section>

    <section class="card card-front" aria-label="Card front">
      <h1 class="company-name">Brantmoor Financial Coaching LLC</h1>
      <div class="contact">
        <p class="contact-person">Dale Brantmoor<br>dale@brantmoorfinancialcoaching.com</p>
        <div class="contact-rule"></div>
        <p class="contact-address">4120 W Sahara Ave #118-B<br>Las Vegas, NV 89102</p>
        <div class="contact-rule"></div>
        <p class="contact-web">brantmoorfinancialcoaching.com<br>702-555-0184</p>
      </div>
    </section>
  </main>
</body>
</html>
```